Mine Engineering Consultancy specializing in
* Pit optimization
* Mine Design
* Scheduling
* Mine Rehabilitation

Mining

RVT Mining Pty Ltd
Dennis Holloway
Director/Principle Mining Engineer
Mobile 0418263591
Email dennis.holloway@rvtmining-example.com

```html
<!DOCTYPE html>
<html lang="en">
<head>
<meta charset="utf-8">
<title>RVT Mining Pty Ltd – Business Cards</title>
<link href="https://fonts.googleapis.com/css2?family=Tinos:wght@400;700&family=Arimo:wght@400&display=swap" rel="stylesheet">
<style>
  :root {
    --page: #e9e6e1;
    --rock-light: #d4d4d4;
    --rock-mid: #a9a9a9;
    --rock-dark: #8a8a8a;
    --brand-blue: #3aa3dc;
    --brand-blue-light: #5bbcea;
    --deep-blue: #1d7fc0;
    --night: #050607;
    --night-soft: #1a1d22;
    --ink: #1c1c1c;
    --white: #ffffff;
  }
  html, body {
    margin: 0;
    padding: 0;
    width: 1200px;
    height: 902px;
    overflow: hidden;
    background: var(--page);
  }
  .canvas {
    position: relative;
    width: 1200px;
    height: 902px;
  }
  .card {
    position: absolute;
    width: 540px;
    height: 310px;
    border-radius: 4px;
    overflow: hidden;
    box-shadow: 0 6px 18px rgba(0,0,0,.25);
  }

  /* Services side */
  .card--services { left: 60px; top: 100px; }
  .services__photo {
    position: absolute; inset: 0;
    background: radial-gradient(ellipse at 60% 40%, var(--rock-light) 0%, var(--rock-mid) 60%, var(--rock-dark) 100%);
  }
  .services__mark {
    position: absolute;
    left: 34px; top: 120px;
    font-family: "Tinos", serif;
    font-weight: 400;
    font-size: 150px;
    line-height: 1;
    color: var(--brand-blue);
    letter-spacing: 2px;
  }
  .services__heading {
    position: absolute;
    right: 64px; top: 38px;
    margin: 0;
    font-family: "Tinos", serif;
    font-weight: 400;
    font-size: 32px;
    color: var(--brand-blue);
    letter-spacing: 1px;
  }
  .services__list {
    position: absolute;
    right: 36px; top: 96px;
    margin: 0; padding: 0;
    list-style: none;
    text-align: right;
    font-family: "Tinos", serif;
    font-size: 22px;
    color: var(--ink);
  }
  .services__list li {
    display: flex;
    justify-content: flex-end;
    align-items: center;
    gap: 14px;
    height: 34px;
  }
  .services__list li::after {
    content: "";
    width: 8px; height: 8px;
    border-radius: 50%;
    background: var(--ink);
    box-shadow: 0 0 0 3px var(--rock-light);
  }

  /* Contact side */
  .card--contact { left: 600px; top: 492px; }
  .contact__bg { position: absolute; inset: 0; }
  .contact__logo {
    position: absolute;
    left: 36px; top: 60px;
    display: flex;
    align-items: baseline;
    gap: 14px;
    font-family: "Tinos", serif;
    font-weight: 400;
    color: var(--brand-blue);
  }
  .contact__logo-mark { font-size: 62px; line-height: 1; }
  .contact__logo-name { font-size: 28px; }
  .contact__person {
    position: absolute;
    left: 34px; top: 222px;
    color: var(--white);
  }
  .contact__name {
    margin: 0;
    font-family: "Tinos", serif;
    font-weight: 700;
    font-size: 32px;
    line-height: 1.1;
  }
  .contact__role {
    margin: 4px 0 0;
    font-family: "Arimo", sans-serif;
    font-size: 14px;
  }
  .contact__divider {
    position: absolute;
    left: 290px; top: 200px;
    width: 1px; height: 76px;
    background: rgba(255,255,255,.7);
  }
  .contact__details {
    position: absolute;
    left: 304px; top: 210px;
    margin: 0; padding: 0;
    list-style: none;
    font-family: "Arimo", sans-serif;
    font-size: 12.5px;
    color: var(--white);
  }
  .contact__details li {
    display: flex;
    align-items: center;
    gap: 8px;
    height: 26px;
  }
  .contact__details svg { flex: none; }
</style>
</head>
<body>
<main class="canvas">

  <section class="card card--services" aria-label="Card back – services">
    <div class="services__photo" role="img" aria-label="Photograph of an open-pit mine with a haul truck on the ramp"></div>
    <div class="services__mark">RVT</div>
    <h2 class="services__heading">SERVICES</h2>
    <ul class="services__list">
      <li>Pit optimization</li>
      <li>Mine Design</li>
      <li>Scheduling</li>
      <li>Mine Rehabilitation</li>
    </ul>
  </section>

  <section class="card card--contact" aria-label="Card front – contact">
    <svg class="contact__bg" width="540" height="310" viewBox="0 0 540 310" aria-hidden="true">
      <defs>
        <linearGradient id="blueFill" x1="0" y1="0" x2="1" y2="1">
          <stop offset="0" stop-color="#2fa6e6"/>
          <stop offset="1" stop-color="#1b78bb"/>
        </linearGradient>
        <linearGradient id="nightFill" x1="0" y1="0" x2="1" y2="1">
          <stop offset="0" stop-color="#1a1d22"/>
          <stop offset="0.6" stop-color="#050607"/>
        </linearGradient>
      </defs>
      <rect width="540" height="310" fill="url(#blueFill)"/>
      <polygon points="0,0 540,0 540,30 512,112 478,150 0,160" fill="url(#nightFill)"/>
      <polyline points="60,170 482,160 518,120 540,58" fill="none" stroke="#3aa3dc" stroke-width="7"/>
    </svg>
    <div role="img" aria-label="Contour plan of a mine pit" style="position:absolute;left:0;top:0;width:540px;height:150px;background:linear-gradient(180deg,rgba(40,44,60,.35),rgba(0,0,0,0));"></div>

    <div class="contact__logo">
      <span class="contact__logo-mark">RVT</span>
      <span class="contact__logo-name">Mining Pty Ltd</span>
    </div>

    <div class="contact__person">
      <h1 class="contact__name">Dennis Holloway</h1>
      <p class="contact__role">Director/Principle Mining Engineer</p>
    </div>

    <div class="contact__divider"></div>

    <ul class="contact__details">
      <li>
        <svg width="14" height="14" viewBox="0 0 14 14" aria-label="Mobile"><rect x="3.5" y="1" width="7" height="12" rx="1.5" fill="none" stroke="#fff" stroke-width="1.4"/><circle cx="7" cy="11" r=".9" fill="#fff"/></svg>
        <span>0418263591</span>
      </li>
      <li>
        <svg width="14" height="14" viewBox="0 0 14 14" aria-label="Email"><rect x="1" y="3" width="12" height="8" fill="none" stroke="#fff" stroke-width="1.4"/><polyline points="1,3 7,8 13,3" fill="none" stroke="#fff" stroke-width="1.4"/></svg>
        <span>dennis.holloway@rvtmining-example.com</span>
      </li>
    </ul>
  </section>

</main>
</body>
</html>
```